CD Cover (EDM, Tropical, Urban) Home and biscuit CD (electronic music tropica, urban, ethnic)

We seek a tropical design, ethnic, wild, colorful, etc ... for an album of electronic music with those same characteristics. Attached indicative examples of what we would like. The music is similar to that of the examples, not only the cover we seek. The title of the CD is as follows: TOLUVE RESPIRADOS PRESENTS KOB Thanks! -------------------------------- Looking for a tropical, ethnic, colorful design ... for a music CD. We attached examples of what kind of design we want. The music of esta CD is similar to the examples, not only in the cover, Also the music. The title of the CD (the only text) is: TOLUVE RESPIRADOS PRESENTS KOB Thanks! ------------------------------

Target Market(s)

Young audience, consumer electronic music / Young people, music EDM Consumers

Industry/Entity Type

Music Download

Font styles to use
Serif

Requirements
Must have
• To resemble any of the accompanying examples, serve. / Like the attached examples.
Nice to have

```html
<!DOCTYPE html>
<html lang="es">
<head>
<meta charset="utf-8">
<title>Toluve Respirados presenta KOB</title>
<link rel="stylesheet" href="https://fonts.googleapis.com/css2?family=Zilla+Slab:wght@700&display=swap">
<style>
  :root {
    --page: #ffffff;
    --tone-top: #0fd48d;
    --tone-mid: #48e16a;
    --tone-low: #b4ec2a;
    --tone-bottom: #f2f512;
    --shade-green: rgba(8, 150, 96, 0.35);
    --shade-olive: rgba(120, 150, 20, 0.35);
    --glow-lime: rgba(190, 255, 120, 0.35);
    --label-disc: #ffffff;
    --title-ink: #10bf86;
    --presenter-ink: #ffffff;
  }
  html, body {
    margin: 0;
    padding: 0;
    width: 1200px;
    height: 1200px;
    overflow: hidden;
    background: var(--page);
  }
  .cover-canvas {
    position: relative;
    width: 1200px;
    height: 1200px;
    background: var(--page);
  }
  .cover-art {
    position: absolute;
    left: 82px;
    top: 72px;
    width: 1044px;
    height: 1046px;
    background:
      radial-gradient(circle at 18% 20%, var(--shade-green) 0, transparent 22%),
      radial-gradient(circle at 78% 14%, var(--shade-green) 0, transparent 18%),
      radial-gradient(circle at 84% 42%, var(--glow-lime) 0, transparent 20%),
      radial-gradient(circle at 12% 55%, var(--glow-lime) 0, transparent 18%),
      radial-gradient(ellipse 30% 35% at 82% 78%, var(--shade-olive) 0, transparent 100%),
      radial-gradient(ellipse 26% 24% at 22% 70%, var(--shade-olive) 0, transparent 100%),
      radial-gradient(circle at 46% 95%, var(--shade-olive) 0, transparent 20%),
      linear-gradient(180deg,
        var(--tone-top) 0%,
        var(--tone-mid) 45%,
        var(--tone-low) 75%,
        var(--tone-bottom) 100%);
  }
  .presenter-line {
    position: absolute;
    left: 82px;
    width: 1044px;
    top: 84px;
    margin: 0;
    text-align: center;
    font-family: "Zilla Slab", serif;
    font-weight: 700;
    font-size: 31px;
    line-height: 1;
    letter-spacing: 0.5px;
    color: var(--presenter-ink);
  }
  .label-disc {
    position: absolute;
    left: 362px;
    top: 360px;
    width: 478px;
    height: 478px;
    border-radius: 50%;
    background: var(--label-disc);
    display: flex;
    align-items: center;
    justify-content: center;
  }
  .album-title {
    margin: 0;
    font-family: "Zilla Slab", serif;
    font-weight: 700;
    font-size: 168px;
    line-height: 1;
    letter-spacing: -2px;
    color: var(--title-ink);
    transform: translateY(-4px);
  }
</style>
</head>
<body>
  <main class="cover-canvas">
    <div class="cover-art" role="img" aria-label="Ornate tropical paisley and mandala pattern in a green to yellow gradient"></div>
    <p class="presenter-line">TOLUVE RESPIRADOS PRESENTA</p>
    <div class="label-disc">
      <h1 class="album-title">KOB</h1>
    </div>
  </main>
</body>
</html>
```